Business card design for holistic health care clinic

We need a double-sided business card design for our holistic health care clinic that integrates our logo design and also its color scheme. My business is called Veluma. It is an integrative medicine clinic. You have already done the logo for me. Please ensure an elegant and upscale design that is not cluttered, but still has all the necessary information (please see below for details).

Target Market(s)

Wellness, fitness, rehabilitation for educated, well-traveled open-minded clients who are focused on natural, organic, balanced and preventive healthcare and lifestyle.

Industry/Entity Type

Medical

Contact Information for Business Card

Modern, clean.

Number of Pages Required

1 page

Font styles to use
Serif
Sans Serif

Colors

Designer to choose colors to be used in the design.

Requirements
Must have
• Logo on one side, all other information on the other side.
• Other information should include:
• Tomas Brevik - ND, CSCS, LMT
• 4120 North Harlow Street
• Austin, TX 78631
• 512 608 2947
• 818 459 7208
• info@VelumaHealth.com
• t.brevik@VelumaHealth.com
Nice to have
• Darker background on front - but not totally black - shaded/dark gray.

```html
<!DOCTYPE html>
<html lang="en">
<head>
<meta charset="utf-8">
<title>Veluma Business Card</title>
<link href="https://fonts.googleapis.com/css2?family=PT+Sans:ital,wght@0,400;0,700;1,400;1,700&display=swap" rel="stylesheet">
<style>
  :root {
    --backdrop: #5a4838;
    --card-dark: #262626;
    --brand-blue: #0a8bc9;
    --paper: #ecebeb;
    --white: #ffffff;
    --tagline-grey: #4a4a4a;
  }
  * { margin: 0; padding: 0; box-sizing: border-box; }
  html, body { width: 1200px; height: 808px; overflow: hidden; }
  body {
    background: var(--backdrop);
    font-family: "PT Sans", Arial, sans-serif;
    position: relative;
  }
  .card {
    position: absolute;
    width: 505px;
    height: 288px;
    overflow: hidden;
    box-shadow: 0 3px 6px rgba(0,0,0,0.45);
  }
  .card--front { left: 351px; top: 95px; background: var(--card-dark); }
  .card--back  { left: 349px; top: 398px; background: var(--paper); }

  .wave { position: absolute; inset: 0; width: 505px; height: 288px; }

  .brand { position: absolute; color: var(--brand-blue); }
  .brand__name {
    display: block;
    font-weight: 700;
    font-size: 52px;
    line-height: 1;
    letter-spacing: 1px;
  }
  .brand__line {
    display: block;
    font-weight: 700;
    font-size: 14.5px;
    margin-top: 4px;
    letter-spacing: 0.2px;
  }
  .card--front .brand { left: 43px; top: 64px; }
  .card--back .brand { left: 0; right: 0; top: 120px; text-align: center; }
  .card--back .brand__name { font-size: 56px; }
  .card--back .brand__line { font-size: 15.5px; }

  .contact {
    position: absolute;
    right: 21px;
    top: 160px;
    text-align: right;
    color: var(--white);
  }
  .contact__name { font-size: 17px; font-weight: 700; letter-spacing: 0.2px; margin-bottom: 9px; }
  .contact__creds { font-size: 10px; }
  .contact__row {
    display: flex; justify-content: flex-end; align-items: center;
    font-size: 12.5px; line-height: 16px; gap: 6px;
  }
  .contact__row svg { width: 11px; height: 11px; fill: var(--white); flex: none; }
  .contact__address { font-size: 12.5px; line-height: 18px; }

  .tagline {
    position: absolute; left: 0; right: 0; top: 236px;
    text-align: center; font-style: italic; font-weight: 700;
    font-size: 12.5px; color: var(--tagline-grey);
  }
</style>
</head>
<body>

<section class="card card--front">
  <svg class="wave" viewBox="0 0 505 288" aria-hidden="true">
    <path d="M0,196 C70,232 150,228 240,170 C330,110 410,72 505,72 L505,288 L0,288 Z" fill="#0a8bc9"/>
    <path d="M0,218 C90,262 170,252 262,188 C350,128 430,96 505,102 L505,108 C430,104 356,136 272,196 C182,262 86,272 0,232 Z" fill="#262626"/>
  </svg>

  <div class="brand">
    <span class="brand__name">VELUMA</span>
    <span class="brand__line">Integrative Holistic Medicine</span>
  </div>

  <div class="contact">
    <p class="contact__name">TOMAS BREVIK <span class="contact__creds">- ND, CSCS, LMT</span></p>
    <p class="contact__row">512 608 2947
      <svg viewBox="0 0 12 12"><path d="M1,4 C1,2 3,1 6,1 C9,1 11,2 11,4 L9,5 L8,3.5 L4,3.5 L3,5 Z M3,6 L9,6 L10.5,11 L1.5,11 Z"/></svg>
    </p>
    <p class="contact__row">818 459 7208
      <svg viewBox="0 0 12 12"><path d="M3,0 H9 V12 H3 Z M4,1.5 V9 H8 V1.5 Z" fill-rule="evenodd"/></svg>
    </p>
    <p class="contact__row">t.brevik@VelumaHealth.com
      <svg viewBox="0 0 12 12"><path d="M0,2.5 H12 V3.2 L6,7 L0,3.2 Z M0,4.5 L6,8.3 L12,4.5 V9.5 H0 Z"/></svg>
    </p>
    <p class="contact__row">www.VelumaHealth.com
      <svg viewBox="0 0 12 12"><circle cx="6" cy="6" r="5.5"/></svg>
    </p>
    <p class="contact__address">4120 North Harlow Street ,Austin, TX 78631</p>
  </div>
</section>

<section class="card card--back">
  <div class="brand">
    <span class="brand__name">VELUMA</span>
    <span class="brand__line">Integrative Holistic Medicine</span>
  </div>
  <p class="tagline">your wellness, your way – care shaped around you</p>
</section>

</body>
</html>
```